" Somos uma empresa afiliada a Lumira Capital e representamos ela em Cuiabá. Prestamos o serviço de assessoria em investimentos a clientes de alto poder aquisitivo, um público private. Serviço exclusivo de "

```html
<!DOCTYPE html>
<html lang="pt-BR">
<head>
<meta charset="utf-8">
<title>Assinatura de e-mail – Veltra Investimentos</title>
<link rel="stylesheet" href="https://fonts.googleapis.com/css2?family=Cinzel:wght@400;600&family=Lato:wght@400;700&display=swap">
<style>
  :root{
    --page:#eef0f3;
    --navy:#0b1424;
    --navy-deep:#060c17;
    --silver:#e9eaec;
    --silver-light:#f7f7f8;
    --gold:#c9a55a;
    --gold-light:#e6cf95;
    --ink:#151a24;
    --muted:#5b606a;
  }
  *{box-sizing:border-box;margin:0;padding:0}
  html,body{width:1200px;height:1200px;overflow:hidden;background:var(--page)}
  .signature{
    position:absolute;left:30px;top:505px;width:1140px;height:190px;
    box-shadow:0 10px 30px rgba(0,0,0,.12);
  }
  .signature-bg{position:absolute;inset:0}
  .brand{
    position:absolute;left:60px;top:0;height:178px;width:300px;
    display:flex;align-items:center;gap:16px;
  }
  .brand-square{width:22px;height:22px;background:var(--gold)}
  .brand-name{
    font-family:"Cinzel",serif;font-weight:400;color:var(--silver-light);
    font-size:44px;line-height:1;letter-spacing:1px;
  }
  .brand-name small{display:block;font-size:15px;letter-spacing:3px;margin-top:6px}
  .person{position:absolute;left:412px;top:70px;width:240px}
  .person-name{font-family:"Cinzel",serif;font-size:22px;color:var(--ink);letter-spacing:.5px;white-space:nowrap}
  .person-role{font-family:"Lato",sans-serif;font-weight:700;font-size:17px;color:var(--ink);margin-top:2px}
  .divider{position:absolute;left:672px;top:22px;width:1px;height:138px;background:#9da1a8}
  .contacts{position:absolute;left:700px;top:18px;list-style:none;font-family:"Lato",sans-serif;color:var(--ink)}
  .contacts li{display:flex;align-items:flex-start;gap:12px;font-size:15px;line-height:1.3}
  .contacts li + li{margin-top:10px}
  .contacts svg{flex:0 0 26px;width:26px;height:26px}
  .partner{
    position:absolute;left:920px;top:60px;display:flex;align-items:center;gap:12px;
  }
  .partner-square{width:44px;height:44px;background:var(--navy)}
  .partner-text{font-family:"Lato",sans-serif;color:var(--muted)}
  .partner-name{font-size:17px;font-weight:700;color:var(--ink)}
  .partner-note{font-size:10px;letter-spacing:.5px;line-height:1.3;margin-top:3px;text-transform:uppercase}
</style>
</head>
<body>
<div class="signature">
  <svg class="signature-bg" viewBox="0 0 1140 190" preserveAspectRatio="none">
    <defs>
      <linearGradient id="navyFill" x1="0" y1="0" x2="1" y2="1">
        <stop offset="0" stop-color="#0b1424"/><stop offset="1" stop-color="#060c17"/>
      </linearGradient>
      <linearGradient id="silverFill" x1="0" y1="0" x2="1" y2="0">
        <stop offset="0" stop-color="#f4f4f5"/><stop offset=".6" stop-color="#e6e7e9"/><stop offset="1" stop-color="#f8f8f9"/>
      </linearGradient>
      <linearGradient id="goldFill" x1="0" y1="0" x2="1" y2="0">
        <stop offset="0" stop-color="#9c7a35"/><stop offset=".5" stop-color="#e6cf95"/><stop offset="1" stop-color="#b38d45"/>
      </linearGradient>
    </defs>
    <rect width="1140" height="190" fill="url(#silverFill)"/>
    <polygon points="900,0 1140,0 1140,178 1010,178" fill="#ffffff" opacity=".45"/>
    <polygon points="0,0 388,0 372,178 0,178" fill="url(#navyFill)"/>
    <rect y="178" width="1140" height="12" fill="url(#goldFill)"/>
  </svg>

  <div class="brand">
    <span class="brand-square"></span>
    <div class="brand-name">VELTRA<small>INVESTIMENTOS</small></div>
  </div>

  <div class="person">
    <div class="person-name">NOME COMPLETO</div>
    <div class="person-role">Cargo</div>
  </div>

  <div class="divider"></div>

  <ul class="contacts">
    <li>
      <svg viewBox="0 0 26 26"><circle cx="13" cy="13" r="13" fill="#151a24"/><path d="M9 7.5l2.3-.4 1.2 3-1.5 1.1a7 7 0 0 0 3.6 3.6l1.1-1.5 3 1.2-.4 2.3c-5.3.4-9.7-4-9.3-9.3z" fill="#fff"/></svg>
      <span>(xx) xxxx-xxxx</span>
    </li>
    <li>
      <svg viewBox="0 0 26 26"><circle cx="13" cy="13" r="13" fill="#151a24"/><path d="M13 6.5a4.5 4.5 0 0 0-4.5 4.5c0 3.3 4.5 8.5 4.5 8.5s4.5-5.2 4.5-8.5A4.5 4.5 0 0 0 13 6.5zm0 6.2a1.7 1.7 0 1 1 0-3.4 1.7 1.7 0 0 1 0 3.4z" fill="#fff"/></svg>
      <span>Seu endereço - Bairro<br>Cidade - Estado<br>CEP 000-0000</span>
    </li>
    <li>
      <svg viewBox="0 0 26 26"><circle cx="13" cy="13" r="13" fill="#151a24"/><rect x="7" y="8.5" width="12" height="9" rx="1" fill="#fff"/><path d="M7.5 9l5.5 4.5L18.5 9" fill="none" stroke="#151a24" stroke-width="1.2"/></svg>
      <span>seuemail@exemplo.com</span>
    </li>
  </ul>

  <div class="partner">
    <span class="partner-square"></span>
    <div class="partner-text">
      <div class="partner-name">Lumira Capital</div>
      <div class="partner-note">Agente autônomo<br>de investimentos</div>
    </div>
  </div>
</div>
</body>
</html>
```